Need Powerpoint masters for my consulting company in privacy (RGPD) and IT

For my newly created consulting company I need powerpoint slides masters.
The company is specialzed in privacy (RGPD) and IT.
The company already has a logo (obtained via Pixelhive).
These master slides will be mainly used when presenting reports/analysis to clients.
I'll attach a PNG files of the logo.

```html
<!DOCTYPE html>
<html lang="en">
<head>
<meta charset="utf-8">
<title>Lucien Morel Conseil – Slide Masters</title>
<link href="https://fonts.googleapis.com/css2?family=Roboto:wght@400;500;700&display=swap" rel="stylesheet">
<style>
:root{
  --navy:#0b2d4a;
  --deep:#062f4c;
  --teal:#0e8c98;
  --teal-dark:#0a6f7c;
  --text:#555b61;
  --white:#ffffff;
  --step1:#f3a83b;
  --step2:#df3f7a;
  --step3:#6a3d95;
  --step4:#14a3aa;
  --step5:#3ccbd4;
  --bulb-orange:#d9581a;
  --bulb-navy:#2f4a66;
}
*{box-sizing:border-box;margin:0;padding:0}
html,body{width:1200px;height:1060px;overflow:hidden}
body{
  position:relative;
  font-family:"Roboto",Arial,sans-serif;
  background:radial-gradient(ellipse at center,#8c8c8c 0%,#6a6a6a 60%,#4f4f4f 100%);
}
.slide{
  position:absolute;width:533px;height:300px;background:var(--white);overflow:hidden;
  box-shadow:0 10px 22px rgba(0,0,0,.45);
}
.s-welcome{left:53px;top:53px}
.s-bulb{left:613px;top:53px}
.s-toc{left:53px;top:380px}
.s-steps{left:613px;top:380px}
.s-team{left:53px;top:707px}
.s-thanks{left:613px;top:707px;background:linear-gradient(120deg,#0c7f90 0%,#0a5f7c 50%,#073a5a 100%)}

.brand{position:absolute;display:flex;align-items:center;gap:5px;color:var(--teal-dark);font-weight:500;white-space:nowrap}
.brand .mark{background:var(--teal-dark);flex:none}
.brand-small{right:22px;top:22px;font-size:10.5px}
.brand-small .mark{width:9px;height:9px}

.page-title{position:absolute;left:25px;top:20px;font-size:22px;font-weight:700;color:var(--navy)}

/* welcome */
.s-welcome .brand{left:32px;top:48px;font-size:16px}
.s-welcome .brand .mark{width:14px;height:14px}
.welcome-title{position:absolute;left:32px;top:136px;font-size:29px;font-weight:700;color:var(--navy)}
.welcome-text{position:absolute;left:32px;top:184px;width:232px;font-size:11px;line-height:18.7px;color:var(--text)}
.welcome-art{position:absolute;left:0;top:0}

/* bulb */
.bulb-art{position:absolute;left:20px;top:64px;width:254px;height:222px;border-radius:18px;
  background:linear-gradient(160deg,#e9eef3 0%,#c9d3dd 35%,#e7a27a 75%,var(--bulb-orange) 100%)}
.bulb-text{position:absolute;left:301px;top:94px;width:212px;font-size:12.3px;line-height:20px;color:var(--text)}

/* toc */
.toc-list{position:absolute;left:25px;top:78px;list-style:none}
.toc-list li{display:flex;align-items:center;height:34px;font-size:21px;color:var(--text)}
.toc-list svg{width:21px;height:21px;margin-right:29px}
.toc-art{position:absolute;left:301px;top:84px;width:223px;height:207px;border-radius:14px;
  background:linear-gradient(135deg,#0c3553 0%,#0b5a70 45%,#168b8a 80%,#2aa08d 100%)}

/* steps */
.flow{position:absolute;left:0;top:0}
.step{position:absolute;top:127px;width:85px}
.step-tag{height:23px;border-radius:12px;color:#fff;font-size:10px;font-weight:700;display:flex;align-items:center;justify-content:center;border:1.5px solid #fff;box-shadow:0 0 0 1px #9aa}
.step-box{height:86px;border:1px solid #555;border-top:none;border-radius:0 0 8px 8px;text-align:center;padding-top:14px}
.step-box h3{font-size:9px;font-weight:500;color:#222}
.step-box p{font-size:5.8px;line-height:8.2px;color:#666;margin-top:5px;padding:0 4px}

/* team */
.team-band{position:absolute;left:0;top:150px;width:533px;height:150px;background:linear-gradient(90deg,#0d8a97 0%,#0a6985 55%,#062d4d 100%)}
.member{position:absolute;top:72px;width:160px;text-align:center;color:#fff}
.member .photo{width:128px;height:128px;margin:0 auto;border-radius:50%;
  background:radial-gradient(circle at 50% 45%,#c9c4bd 0%,#9a9894 60%,#6f7377 100%);box-shadow:0 0 0 4px #fff,0 0 0 5px #0d8a97}
.member h4{margin-top:19px;font-size:16.5px;font-weight:700}
.member span{display:block;font-size:13px;margin-top:1px}
.member .social{display:flex;justify-content:center;gap:8px;margin-top:10px}
.member .social i{width:7px;height:7px;border-radius:50%;background:#fff;display:block}

/* thanks */
.thanks-art{position:absolute;left:29px;top:50px;width:220px;height:230px;border-radius:50%;
  background:radial-gradient(circle,#3c9fb0 0%,#2a8ba3 40%,rgba(20,110,140,.4) 70%,rgba(12,90,120,0) 100%)}
.thanks-brand{position:absolute;left:258px;top:140px;width:262px;text-align:center;color:#fff;font-size:23px;font-weight:500}
.thanks-rule{position:absolute;left:262px;top:176px;width:254px;height:1px;background:#fff}
.thanks-title{position:absolute;left:258px;top:201px;width:262px;text-align:center;color:#fff;font-size:19px;font-weight:700}
</style>
</head>
<body>

<section class="slide s-welcome">
  <svg class="welcome-art" width="533" height="300" viewBox="0 0 533 300">
    <polygon points="345,0 437,0 300,300 250,300" fill="#062f4c"/>
    <polygon points="437,0 498,0 264,300 300,300" fill="#0e8c98"/>
    <polygon points="498,0 533,0 533,300 264,300" fill="#8d8a84" role="img" aria-label="Photo of consultants smiling around a meeting table"/>
  </svg>
  <div class="brand"><i class="mark"></i>Lucien Morel Conseil</div>
  <h1 class="welcome-title">Welcome</h1>
  <p class="welcome-text">Lorem ipsum dolor sit amet, consectetur adipiscing elit, sed do eiusmod tempor incididunt ut labore et dolore magna aliquaum suspendisse ultrices gravida.</p>
</section>

<section class="slide s-bulb">
  <h2 class="page-title">Page Title Here</h2>
  <div class="brand brand-small"><i class="mark"></i>Lucien Morel Conseil</div>
  <div class="bulb-art" role="img" aria-label="Light bulb infographic with five coloured icon circles"></div>
  <p class="bulb-text">Lorem ipsum dolor sit amet, consectetur adipiscing elit, sed do eiusmod tempor incididunt ut labore et dolore magna aliquuis ipsum suspendisse ultrices gravidisus commodo viverra maecenas accumsan lacus vel ultrices gravidisus commodo viverra maecenas accumsan lacus vel facilisis. facilisis.</p>
</section>

<section class="slide s-toc">
  <h2 class="page-title">Table Of Contents</h2>
  <div class="brand brand-small"><i class="mark"></i>Lucien Morel Conseil</div>
  <ul class="toc-list">
    <li><svg viewBox="0 0 20 20"><circle cx="10" cy="10" r="10" fill="#0e8c98"/><path d="M5.5 10.3l3 3 6-6.3" stroke="#fff" stroke-width="2.2" fill="none"/></svg>Introduction</li>
    <li><svg viewBox="0 0 20 20"><circle cx="10" cy="10" r="10" fill="#0e8c98"/><path d="M5.5 10.3l3 3 6-6.3" stroke="#fff" stroke-width="2.2" fill="none"/></svg>Our Company</li>
    <li><svg viewBox="0 0 20 20"><circle cx="10" cy="10" r="10" fill="#0e8c98"/><path d="M5.5 10.3l3 3 6-6.3" stroke="#fff" stroke-width="2.2" fill="none"/></svg>Our Team</li>
    <li><svg viewBox="0 0 20 20"><circle cx="10" cy="10" r="10" fill="#0e8c98"/><path d="M5.5 10.3l3 3 6-6.3" stroke="#fff" stroke-width="2.2" fill="none"/></svg>Services</li>
    <li><svg viewBox="0 0 20 20"><circle cx="10" cy="10" r="10" fill="#0e8c98"/><path d="M5.5 10.3l3 3 6-6.3" stroke="#fff" stroke-width="2.2" fill="none"/></svg>Analysis</li>
    <li><svg viewBox="0 0 20 20"><circle cx="10" cy="10" r="10" fill="#0e8c98"/><path d="M5.5 10.3l3 3 6-6.3" stroke="#fff" stroke-width="2.2" fill="none"/></svg>Presentation</li>
  </ul>
  <div class="toc-art" role="img" aria-label="Office work photo in teal and navy tones"></div>
</section>

<section class="slide s-steps">
  <h2 class="page-title">Page Title Here</h2>
  <div class="brand brand-small"><i class="mark"></i>Lucien Morel Conseil</div>
  <svg class="flow" width="533" height="300" viewBox="0 0 533 300" fill="none" stroke="#333" stroke-width="0.9">
    <path d="M70 124V110H169V123"/><path d="M166 119l3 4 3-4"/>
    <path d="M268 124V110H366V123"/><path d="M363 119l3 4 3-4"/>
    <path d="M169 246V258H268V245"/><path d="M265 249l3-4 3 4"/>
    <path d="M366 246V258H464V245"/><path d="M461 249l3-4 3 4"/>
  </svg>
  <div class="step" style="left:28px"><div class="step-tag" style="background:var(--step1)">STEP 01</div><div class="step-box"><h3>RERUMCILIS</h3><p>Lorem ipsum dolor sit amet, consectetur adipiscing elit, sed do eiusmod tempor incididunt ut labore et dolore</p></div></div>
  <div class="step" style="left:126px"><div class="step-tag" style="background:var(--step2)">STEP 02</div><div class="step-box"><h3>VOLUPTAT</h3><p>Lorem ipsum dolor sit amet, consectetur adipiscing elit, sed do eiusmod tempor incididunt ut labore et dolore</p></div></div>
  <div class="step" style="left:225px"><div class="step-tag" style="background:var(--step3)">STEP 03</div><div class="step-box"><h3>CUM SOLUT</h3><p>Lorem ipsum dolor sit amet, consectetur adipiscing elit, sed do eiusmod tempor incididunt ut labore et dolore</p></div></div>
  <div class="step" style="left:323px"><div class="step-tag" style="background:var(--step4)">STEP 04</div><div class="step-box"><h3>CORRUPTI</h3><p>Lorem ipsum dolor sit amet, consectetur adipiscing elit, sed do eiusmod tempor incididunt ut labore et dolore</p></div></div>
  <div class="step" style="left:421px"><div class="step-tag" style="background:var(--step5)">STEP 05</div><div class="step-box"><h3>DOLORES</h3><p>Lorem ipsum dolor sit amet, consectetur adipiscing elit, sed do eiusmod tempor incididunt ut labore et dolore</p></div></div>
</section>

<section class="slide s-team">
  <div class="team-band"></div>
  <h2 class="page-title">Our Team</h2>
  <div class="brand brand-small"><i class="mark"></i>Lucien Morel Conseil</div>
  <div class="member" style="left:12px"><div class="photo" role="img" aria-label="Portrait of team member"></div><h4>John Doe</h4><span>odio dignissimos</span><div class="social"><i></i><i></i><i></i></div></div>
  <div class="member" style="left:187px"><div class="photo" role="img" aria-label="Portrait of team member"></div><h4>Smtha John</h4><span>odio dignissimos</span><div class="social"><i></i><i></i><i></i></div></div>
  <div class="member" style="left:361px"><div class="photo" role="img" aria-label="Portrait of team member"></div><h4>John smith</h4><span>odio dignissimos</span><div class="social"><i></i><i></i><i></i></div></div>
</section>

<section class="slide s-thanks">
  <div class="thanks-art" role="img" aria-label="Illustration of a team around a creative idea gear"></div>
  <div class="thanks-brand">Lucien Morel Conseil</div>
  <div class="thanks-rule"></div>
  <div class="thanks-title">THANK YOU</div>
</section>

</body>
</html>
```